Need Letterhead Design & Matching Business Card

I have a logo that I love already. But the letterhead is less than appealing and boring. I'd like a design for my letterhead which I will match with business cards. Also, I'd like to have used fonts that are generally available, as my current letterhead uses a font named "SPACE" which nobody has unless they download it...so when a Word version is forwarded, it looks awful on the receiver's screed due to not having the font. That being said, modern is the look we like and are going for.

My business is "Halloran Brightmoor PC" - a law firm specializing in representing people who have suffered catastrophic injuries or death (plane, auto, train crashes etc.).

See attached letterhead, which has all of the pertinent information. My logo is also attached in various formats.

```html
<!DOCTYPE html>
<html lang="en">
<head>
<meta charset="utf-8">
<title>Halloran Brightmoor PC — Stationery</title>
<link href="https://fonts.googleapis.com/css2?family=Montserrat:wght@400;500;600&family=Fira+Sans:wght@400&display=swap" rel="stylesheet">
<style>
  :root {
    --backdrop: #8e8e8e;
    --ink: #000000;
    --paper: #ffffff;
    --panel: #f4f4f4;
    --mid-grey: #a4a4a4;
    --dark-grey: #444444;
    --contact-text: #333333;
  }
  * { margin: 0; padding: 0; box-sizing: border-box; }
  html, body { width: 1200px; height: 1200px; overflow: hidden; background: var(--backdrop); }
  body { position: relative; font-family: "Montserrat", sans-serif; }

  .piece { position: absolute; overflow: hidden; }

  /* Letterhead */
  .letterhead { left: 47px; top: 42px; width: 512px; height: 731px; background: var(--paper); }
  .letterhead-header { position: absolute; left: 0; top: 0; width: 100%; height: 139px; background: var(--ink); color: var(--paper); }
  .letterhead-firm { position: absolute; left: 32px; top: 28px; font-size: 22px; line-height: 21px; font-weight: 400; }
  .letterhead-contact { position: absolute; left: 33px; top: 76px; font-size: 7.5px; line-height: 10px; font-weight: 500; letter-spacing: 0.4px; text-transform: uppercase; }
  .header-mark { position: absolute; right: 72px; top: 58px; display: flex; align-items: center; gap: 8px; font-size: 13px; font-weight: 400; }
  .mark-square { width: 10px; height: 10px; background: var(--paper); }
  .letterhead-footer-shapes { position: absolute; left: 0; top: 0; }
  .letterhead-footer { position: absolute; left: 9px; top: 647px; color: var(--paper); font-size: 9px; line-height: 15.5px; font-weight: 500; letter-spacing: 0.6px; text-transform: uppercase; }

  /* Dark panels */
  .dark-card { background: var(--ink); color: var(--paper); }
  .letter-back { left: 642px; top: 43px; width: 511px; height: 730px; }
  .card-back { left: 643px; top: 840px; width: 510px; height: 297px; }
  .centered-name { position: absolute; left: 0; width: 100%; text-align: center; font-weight: 400; }
  .letter-back .centered-name { top: 340px; font-size: 30px; }
  .card-back .centered-name { top: 125px; font-size: 24px; }
  .web-address { position: absolute; left: 0; width: 100%; text-align: center; font-weight: 600; font-size: 17px; letter-spacing: 0.2px; padding-left: 28px; }
  .letter-back .web-address { top: 666px; }
  .card-back .web-address { top: 235px; }

  /* Business card front */
  .card-front { left: 47px; top: 841px; width: 512px; height: 297px; background: var(--paper); }
  .card-firm { position: absolute; left: 50px; top: 154px; font-size: 31px; line-height: 30px; font-weight: 400; color: var(--ink); }
  .card-contact-panel { position: absolute; left: 285px; top: 0; width: 227px; height: 100%; background: var(--panel); }
  .contact-row { position: absolute; left: 30px; display: flex; align-items: flex-start; gap: 18px; font-family: "Fira Sans", sans-serif; font-size: 12px; line-height: 15px; color: var(--contact-text); }
  .contact-row svg { width: 24px; height: 18px; flex: none; fill: var(--ink); }
</style>
</head>
<body>

  <section class="piece letterhead">
    <header class="letterhead-header">
      <div class="letterhead-firm">Halloran<br>Brightmoor PC</div>
      <div class="letterhead-contact">
        www.halloranbrightmoor.com<br>
        dana@halloranbrightmoor.com<br>
        Tel:(855) 410-
      </div>
      <div class="header-mark"><span class="mark-square"></span>Halloran Brightmoor</div>
    </header>
    <svg class="letterhead-footer-shapes" width="512" height="731" viewBox="0 0 512 731" aria-hidden="true">
      <polygon points="179,640 512,570 512,731 0,731" fill="var(--mid-grey)"/>
      <polygon points="353,680 512,646 512,731 353,731" fill="var(--dark-grey)"/>
      <polygon points="0,599 512,716 512,731 0,731" fill="var(--ink)"/>
    </svg>
    <div class="letterhead-footer">
      R. Dana Whitcombe, Esq. | President<br>
      4820 Larchmont Ave. | Suite 700<br>
      Fairview Heights, CA 90288
    </div>
  </section>

  <section class="piece dark-card letter-back">
    <div class="centered-name">Halloran Brightmoor</div>
    <div class="web-address">www.halloranbrightmoor.com</div>
  </section>

  <section class="piece card-front">
    <div class="card-firm">Halloran<br>Brightmoor PC</div>
    <div class="card-contact-panel">
      <div class="contact-row" style="top:72px">
        <svg viewBox="0 0 24 18"><path d="M1 1h22v16H1z M2.5 2.5 12 10l9.5-7.5v13h-19z" fill-rule="evenodd"/><path d="M2 2l10 8 10-8v1.5l-10 8-10-8z"/></svg>
        <span>info@email.com</span>
      </div>
      <div class="contact-row" style="top:112px">
        <svg viewBox="0 0 24 24" style="height:22px"><path d="M12 1a7 7 0 0 0-7 7c0 5 7 15 7 15s7-10 7-15a7 7 0 0 0-7-7zm0 9.5A2.5 2.5 0 1 1 12 5.5a2.5 2.5 0 0 1 0 5z"/></svg>
        <span>Main street, Your Loc,<br>Number 12/A, 45678</span>
      </div>
      <div class="contact-row" style="top:155px">
        <svg viewBox="0 0 24 24" style="height:20px"><path d="M6.6 10.8a15 15 0 0 0 6.6 6.6l2.2-2.2a1 1 0 0 1 1-.25 11.4 11.4 0 0 0 3.6.57 1 1 0 0 1 1 1V20a1 1 0 0 1-1 1A17 17 0 0 1 3 4a1 1 0 0 1 1-1h3.5a1 1 0 0 1 1 1c0 1.25.2 2.45.57 3.57a1 1 0 0 1-.25 1z"/></svg>
        <span>+ 012 34 56 789</span>
      </div>
      <div class="contact-row" style="top:193px">
        <svg viewBox="0 0 24 20" style="height:20px"><path d="M12 2C7.5 2 3.5 3.8.5 6.7l1.6 1.6C4.7 5.8 8.2 4.3 12 4.3s7.3 1.5 9.9 4l1.6-1.6C20.5 3.8 16.5 2 12 2zm0 4.6c-3.2 0-6.1 1.3-8.2 3.4l1.6 1.6A9.3 9.3 0 0 1 12 8.9c2.6 0 4.9 1 6.6 2.7l1.6-1.6A11.6 11.6 0 0 0 12 6.6zm0 4.6a7 7 0 0 0-4.9 2l1.6 1.6A4.7 4.7 0 0 1 12 13.5c1.3 0 2.5.5 3.3 1.3l1.6-1.6a7 7 0 0 0-4.9-2zM12 15.5a2 2 0 1 0 0 4 2 2 0 0 0 0-4z"/></svg>
        <span>www.company.com</span>
      </div>
    </div>
  </section>

  <section class="piece dark-card card-back">
    <div class="centered-name">Halloran Brightmoor</div>
    <div class="web-address">www.halloranbrightmoor.com</div>
  </section>

</body>
</html>
```